The most modern business card ever !!!

Our company call “Vantilo”. Vantilo is a technology company specialized in cruises solutions. Out main product is a platform to reserve cruises. This is a revolutionary platform that make easier to travel agencies and final users to reserve cruises across dozen companies like tarvik, welbi, dpv, hbt, etc..We are a “start up”, with a young team of developers and we want to transmit it.. For it, we want something different, a modern business card that represent cruises and technology.. When someone receive this card, this person should say: wowww this is different… this is modern… this is a cruise related company..
Contact Information for Business Card
Requirements
Must have
- diferent, modern
Should not have
- traditions business card

```html
<!DOCTYPE html>
<html lang="en">
<head>
<meta charset="utf-8">
<title>Vantilo business card</title>
<link href="https://fonts.googleapis.com/css2?family=Exo+2:wght@400;500;600;700&display=swap" rel="stylesheet">
<style>
  :root {
    --page-bg: #d9dadb;
    --card-bg: #eef0f0;
    --ink: #1f1f1f;
    --brand-blue: #2ea3d5;
    --panel-black: #121314;
    --soft-white: #e4e6e7;
  }
  html, body {
    margin: 0;
    padding: 0;
    width: 1200px;
    height: 971px;
    overflow: hidden;
    background: var(--page-bg);
    font-family: "Exo 2", sans-serif;
  }
  .card {
    position: absolute;
    left: 100px;
    top: 170px;
    width: 1000px;
    height: 630px;
    border-radius: 28px;
    overflow: hidden;
    background: var(--card-bg);
    box-shadow: 0 18px 40px rgba(0,0,0,0.18);
  }
  .card-shapes {
    position: absolute;
    inset: 0;
  }
  .brand-name {
    position: absolute;
    left: 62px;
    top: 120px;
    margin: 0;
    font-size: 104px;
    font-weight: 600;
    letter-spacing: 1px;
    color: var(--ink);
    line-height: 1;
  }
  .person {
    position: absolute;
    right: 62px;
    top: 262px;
    text-align: right;
  }
  .person-name {
    margin: 0;
    font-size: 38px;
    font-weight: 700;
    color: var(--brand-blue);
    line-height: 1.1;
  }
  .person-role {
    margin: 2px 0 0;
    font-size: 28px;
    font-weight: 400;
    color: var(--soft-white);
  }
  .address {
    position: absolute;
    left: 62px;
    top: 392px;
    margin: 0;
    font-style: normal;
    font-size: 26px;
    line-height: 1.3;
    color: var(--ink);
  }
  .contact-list {
    position: absolute;
    left: 62px;
    top: 500px;
    margin: 0;
    padding: 0;
    list-style: none;
    font-size: 26px;
    line-height: 1.25;
    color: var(--ink);
  }
  .contact-list li {
    display: flex;
    align-items: center;
    gap: 8px;
  }
  .contact-icon {
    width: 22px;
    height: 22px;
    flex: none;
  }
  .web-accent {
    color: var(--brand-blue);
    font-weight: 700;
  }
</style>
</head>
<body>
  <div class="card">
    <svg class="card-shapes" width="1000" height="630" viewBox="0 0 1000 630" aria-hidden="true">
      <polygon class="chevron-band" fill="var(--brand-blue)"
        points="740,0 815,0 565,330 860,630 790,630 465,330"/>
      <polygon class="name-panel" fill="var(--panel-black)"
        points="850,0 1000,0 1000,630 900,630 597,330"/>
    </svg>

    <h1 class="brand-name">Vantilo</h1>

    <div class="person">
      <p class="person-name">Daniel Moreira</p>
      <p class="person-role">Developer</p>
    </div>

    <address class="address">
      R Doutor Paulo Lemos 418<br>
      Sala 14, Vila Serena<br>
      Rio Claro, SP, 13500-310, Brasil
    </address>

    <ul class="contact-list">
      <li>
        <svg class="contact-icon" viewBox="0 0 24 24" aria-hidden="true">
          <path fill="var(--ink)" d="M6.6 10.8a15.1 15.1 0 0 0 6.6 6.6l2.2-2.2a1 1 0 0 1 1-.25 11.4 11.4 0 0 0 3.6.57 1 1 0 0 1 1 1V20a1 1 0 0 1-1 1A17 17 0 0 1 3 4a1 1 0 0 1 1-1h3.5a1 1 0 0 1 1 1c0 1.25.2 2.46.57 3.6a1 1 0 0 1-.25 1z"/>
        </svg>
        (11) 9274-5830
      </li>
      <li>
        <svg class="contact-icon" viewBox="0 0 24 24" aria-hidden="true">
          <rect x="3" y="5" width="18" height="14" fill="none" stroke="var(--ink)" stroke-width="2"/>
          <path d="M3 5l9 8 9-8M3 19l7-6M21 19l-7-6" fill="none" stroke="var(--ink)" stroke-width="2"/>
        </svg>
        nara@vantilo.com.br
      </li>
      <li>
        <svg class="contact-icon" viewBox="0 0 24 24" aria-hidden="true">
          <circle cx="12" cy="12" r="9" fill="none" stroke="var(--brand-blue)" stroke-width="2"/>
          <ellipse cx="12" cy="12" rx="4" ry="9" fill="none" stroke="var(--brand-blue)" stroke-width="1.6"/>
          <path d="M3 12h18M5 7.5h14M5 16.5h14" stroke="var(--brand-blue)" stroke-width="1.6"/>
        </svg>
        <span>www.<span class="web-accent">vantilo</span>.com.br</span>
      </li>
    </ul>
  </div>
</body>
</html>
```